Standard Company Posters / Notices

We have manufacturing sites, across the sites there are notices that managers put up, sometimes like a poster or door notice. These are not in any standard format or follow any standard layout. We wanted to create a notice template that could be adopted with layout guidance for all our internal notices. Some examples of the notices are below. We have three different sites so we would want to interchange the logo to suit the location, I have also added some images used for our values awards as examples of the look we like.

Target Market(s)

Employees

Industry/Entity Type

Food Manufacturing

Requirements
Must have
• Flexible for the site teams to amend to suit their needs.

```html
<!DOCTYPE html>
<html lang="en">
<head>
<meta charset="utf-8">
<title>Site Notice – Mobile Phones</title>
<link href="https://fonts.googleapis.com/css2?family=Montserrat:wght@600;700;800;900&display=swap" rel="stylesheet">
<style>
  :root {
    --page: #ffffff;
    --brand-red: #c8102e;
    --brand-navy: #001e62;
    --brand-surround: #b0b6c3;
    --mono-surround: #d6d6d6;
    --mono-header: #d7d7d7;
    --mono-frame: #000000;
    --mono-text: #636363;
    --ink: #000000;
    --paper: #ffffff;
  }
  html, body {
    margin: 0;
    padding: 0;
    width: 1200px;
    height: 830px;
    overflow: hidden;
    background: var(--page);
  }
  .notice-sheet {
    display: block;
    width: 1200px;
    height: 830px;
    font-family: "Montserrat", sans-serif;
  }
  .headline { font-weight: 900; }
  .subhead { font-weight: 700; }
  .body-line { font-weight: 700; }
  .key-word { font-weight: 700; }
  .site-name { font-weight: 800; }

  .notice--brand .surround { fill: var(--brand-surround); }
  .notice--brand .frame { fill: var(--brand-navy); }
  .notice--brand .panel { fill: var(--paper); }
  .notice--brand .header-band { fill: var(--brand-red); }
  .notice--brand .header-text { fill: var(--paper); }
  .notice--brand .body-line { fill: var(--ink); }
  .notice--brand .key-word { fill: var(--brand-red); }
  .notice--brand .site-name { fill: var(--brand-navy); }
  .notice--brand .site-square { fill: var(--brand-red); }

  .notice--mono .surround { fill: var(--mono-surround); }
  .notice--mono .frame { fill: var(--mono-frame); }
  .notice--mono .panel { fill: var(--paper); }
  .notice--mono .header-band { fill: var(--mono-header); }
  .notice--mono .header-text { fill: var(--ink); }
  .notice--mono .body-line,
  .notice--mono .key-word,
  .notice--mono .site-name { fill: var(--mono-text); }
</style>
</head>
<body>
<svg class="notice-sheet" viewBox="0 0 1200 830" xmlns="http://www.w3.org/2000/svg" role="img" aria-label="Two versions of a site notice: mobile phones are prohibited in this area unless you are authorised and on the concession list">

  <g class="notice notice--brand" transform="translate(29,23)">
    <rect class="surround" x="0" y="0" width="521" height="783" rx="34"/>
    <rect class="frame" x="18" y="20" width="484" height="746" rx="22"/>
    <rect class="panel" x="26" y="27" width="468" height="731" rx="14"/>
    <path class="header-band" d="M26 194 V41 Q26 27 40 27 H480 Q494 27 494 41 V194 Z"/>
    <text class="header-text headline" x="261" y="110" font-size="62" text-anchor="middle" textLength="363" lengthAdjust="spacingAndGlyphs">ATTENTION</text>
    <text class="header-text subhead" x="261" y="162" font-size="58" text-anchor="middle" textLength="220" lengthAdjust="spacingAndGlyphs">PLEASE!</text>

    <text class="body-line" x="261" y="294" font-size="31" text-anchor="middle" textLength="322" lengthAdjust="spacingAndGlyphs">MOBILE PHONES ARE</text>
    <text class="key-word" x="261" y="355" font-size="60" text-anchor="middle" textLength="361" lengthAdjust="spacingAndGlyphs">PROHIBITED</text>
    <text class="body-line" x="261" y="389" font-size="31" text-anchor="middle" textLength="194" lengthAdjust="spacingAndGlyphs">IN THIS AREA</text>
    <text class="body-line" x="261" y="423" font-size="31" text-anchor="middle" textLength="257" lengthAdjust="spacingAndGlyphs">UNLESS YOU ARE</text>
    <text class="key-word" x="261" y="479" font-size="60" text-anchor="middle" textLength="366" lengthAdjust="spacingAndGlyphs">AUTHORISED</text>
    <text class="body-line" x="261" y="516" font-size="31" text-anchor="middle" textLength="190" lengthAdjust="spacingAndGlyphs">AND ON THE</text>
    <text class="body-line" x="261" y="549" font-size="31" text-anchor="middle" textLength="289" lengthAdjust="spacingAndGlyphs">CONCESSION LIST!</text>

    <rect class="site-square" x="160" y="666" width="20" height="20"/>
    <text class="site-name" x="190" y="684" font-size="24">Hartwell &amp; Sons</text>
  </g>

  <g class="notice notice--mono" transform="translate(648,23)">
    <rect class="surround" x="0" y="0" width="521" height="783" rx="34"/>
    <rect class="frame" x="18" y="20" width="484" height="746" rx="22"/>
    <rect class="panel" x="26" y="27" width="468" height="731" rx="14"/>
    <path class="header-band" d="M26 194 V41 Q26 27 40 27 H480 Q494 27 494 41 V194 Z"/>
    <text class="header-text headline" x="261" y="110" font-size="62" text-anchor="middle" textLength="363" lengthAdjust="spacingAndGlyphs">ATTENTION</text>
    <text class="header-text subhead" x="261" y="162" font-size="58" text-anchor="middle" textLength="220" lengthAdjust="spacingAndGlyphs">PLEASE!</text>

    <text class="body-line" x="261" y="294" font-size="31" text-anchor="middle" textLength="322" lengthAdjust="spacingAndGlyphs">MOBILE PHONES ARE</text>
    <text class="key-word" x="261" y="355" font-size="60" text-anchor="middle" textLength="361" lengthAdjust="spacingAndGlyphs">PROHIBITED</text>
    <text class="body-line" x="261" y="389" font-size="31" text-anchor="middle" textLength="194" lengthAdjust="spacingAndGlyphs">IN THIS AREA</text>
    <text class="body-line" x="261" y="423" font-size="31" text-anchor="middle" textLength="257" lengthAdjust="spacingAndGlyphs">UNLESS YOU ARE</text>
    <text class="key-word" x="261" y="479" font-size="60" text-anchor="middle" textLength="366" lengthAdjust="spacingAndGlyphs">AUTHORISED</text>
    <text class="body-line" x="261" y="516" font-size="31" text-anchor="middle" textLength="190" lengthAdjust="spacingAndGlyphs">AND ON THE</text>
    <text class="body-line" x="261" y="549" font-size="31" text-anchor="middle" textLength="289" lengthAdjust="spacingAndGlyphs">CONCESSION LIST!</text>

    <text class="site-name" x="261" y="700" font-size="24" text-anchor="middle">Hartwell Foods Packing</text>
  </g>
</svg>
</body>
</html>
```